VORN - Business cards

Business card to be created for Commercial sales staff

Target Market(s)

Commercial businesses

Industry/Entity Type

Commercial

Contact Information for Business Card

Look professional. For commercial clients

Colors
ffffff

Requirements
Must have
• - Vorn Logo
• - Commercial sales staff as postion
• - room for commerical sales manager role
• - person name and their mobile number
• - Website : vornelectrical.com.au
Nice to have
• White background.
• On back of business card just have the logo no other information
Should not have
• Should only have white background on front of card.

```html
<!DOCTYPE html>
<html lang="en">
<head>
<meta charset="utf-8">
<title>VORN – Business Cards</title>
<link rel="stylesheet" href="https://fonts.googleapis.com/css2?family=Poppins:wght@400;600;800&display=swap">
<style>
  :root {
    --page-bg: #e6e6e6;
    --card-bg: #313438;
    --card-edge: #3b3e43;
    --brand-red: #c4161c;
    --text-white: #ffffff;
    --text-soft: #e3e4e6;
  }
  * { box-sizing: border-box; margin: 0; padding: 0; }
  html, body {
    width: 1200px; height: 900px; overflow: hidden;
    background: var(--page-bg);
    font-family: "Poppins", sans-serif;
  }
  .canvas { position: relative; width: 1200px; height: 900px; }
  .card {
    position: absolute;
    width: 560px; height: 320px;
    background: var(--card-bg);
    border-radius: 22px;
    overflow: hidden;
    box-shadow: 0 18px 40px rgba(0,0,0,.25);
  }
  .card-back { left: 70px; top: 90px; display: flex; align-items: center; justify-content: center; }
  .card-front { left: 570px; top: 480px; }

  .wordmark {
    display: flex; align-items: center; gap: 16px;
  }
  .wordmark-dot {
    width: 54px; height: 54px; border-radius: 50%;
    background: var(--brand-red);
  }
  .wordmark-name {
    font-weight: 800; font-size: 72px; line-height: 1;
    color: var(--text-white); letter-spacing: 1px;
  }

  .front-mark {
    position: absolute; left: -70px; top: 40px;
    width: 330px; height: 330px; border-radius: 50%;
    background: var(--brand-red);
  }
  .front-mark-name {
    position: absolute; left: 60px; top: 130px;
    font-weight: 800; font-size: 64px; line-height: 1;
    color: var(--text-white);
  }

  .contact { position: absolute; left: 318px; top: 44px; width: 230px; }
  .contact-name {
    font-weight: 600; font-size: 17px; color: var(--text-white);
    letter-spacing: .5px; text-transform: uppercase;
  }
  .contact-role { font-size: 12.5px; color: var(--brand-red); margin-top: 1px; }
  .contact-address { font-size: 11.5px; color: var(--text-soft); line-height: 1.35; margin-top: 28px; }
  .contact-list { list-style: none; margin-top: 14px; }
  .contact-list li {
    display: flex; align-items: center; gap: 9px;
    font-size: 11.5px; color: var(--text-soft); line-height: 1.85;
  }
  .contact-list svg { width: 11px; height: 11px; fill: var(--brand-red); flex: none; }
  .contact-list .web { color: var(--text-soft); }
  .contact-list .web span { color: var(--brand-red); }
</style>
</head>
<body>
<main class="canvas">

  <section class="card card-back" aria-label="Business card back">
    <div class="wordmark">
      <span class="wordmark-dot"></span>
      <span class="wordmark-name">VORN</span>
    </div>
  </section>

  <section class="card card-front" aria-label="Business card front">
    <div class="front-mark"></div>
    <span class="front-mark-name">VORN</span>

    <div class="contact">
      <h1 class="contact-name">Marco T Reyes</h1>
      <p class="contact-role">Commercial sales staff</p>
      <p class="contact-address">4120 Brookline Ave #114<br>Tampa, FL 33607</p>
      <ul class="contact-list">
        <li>
          <svg viewBox="0 0 12 12"><path d="M2 1h3l1 3-1.5 1a6 6 0 0 0 2.5 2.5L8 6l3 1v3a1 1 0 0 1-1 1A9 9 0 0 1 1 2a1 1 0 0 1 1-1z"/></svg>
          (555) 014-2286
        </li>
        <li>
          <svg viewBox="0 0 12 12"><path d="M3 0h6a1 1 0 0 1 1 1v10a1 1 0 0 1-1 1H3a1 1 0 0 1-1-1V1a1 1 0 0 1 1-1zm0 2v7h6V2z"/></svg>
          (555) 014-2286
        </li>
        <li>
          <svg viewBox="0 0 12 12"><path d="M0 5l12-5-5 12-1.5-5.5z"/></svg>
          info@vornelectrical.com
        </li>
        <li class="web">
          <svg viewBox="0 0 12 12"><circle cx="6" cy="6" r="5.5"/></svg>
          www.<span>vornelectrical.com.au</span>
        </li>
      </ul>
    </div>
  </section>

</main>
</body>
</html>
```